Vectorline Solutions Web Design Project

Web design for a company that highlights the people and experience behind a company that develops solutions, both through the provision of professional services, as well as software development, using mathematical optimisation tools. We want it to be professional looking (minimal bright flashy colors and animation) and allow us to easily update it after delivery without having to purchase any 3rd party software tools. Minimum tabs: About us, services, products, careers, contact. Search box to search site content, including ad-hoc documents add to site (PDF).
The design should emphasis simplicity and professionalism. We need to be able to link documents to the site easily as we add research papers, project descriptions, key personnel resume's etc etc.
Target Market(s)
Technical professionals, researchers, academics
Industry/Entity Type
Software

```html
<!DOCTYPE html>
<html lang="en">
<head>
<meta charset="utf-8">
<title>Vectorline Solutions</title>
<link href="https://fonts.googleapis.com/css2?family=Arimo:wght@400;700&family=Questrial&family=Hind:wght@500;600;700&display=swap" rel="stylesheet">
<style>
:root{
  --red:#c4250f;
  --red-text:#b8261a;
  --orange:#e8760c;
  --ink:#222;
  --body:#333;
  --muted:#555;
  --rule:#d6d6d6;
  --footer:#2b2b2b;
  --strategy:#c6b80e;
  --success:#c99a12;
  --goal:#c8650f;
}
*{margin:0;padding:0;box-sizing:border-box}
html,body{width:1043px;height:1200px;overflow:hidden;background:#fff}
body{font-family:"Arimo",Arial,sans-serif;color:var(--body)}
.page{position:relative;width:1043px;height:1200px;overflow:hidden}

.site-header{position:absolute;left:0;top:0;width:1043px;height:126px;background:linear-gradient(#e9e9e9,#f7f7f7 70%,#fff)}
.brand{position:absolute;left:106px;top:72px;display:flex;align-items:center;gap:8px}
.brand-dot{width:20px;height:20px;border-radius:50%;background:var(--orange)}
.brand-name{font-family:"Questrial",sans-serif;font-size:21px;color:var(--ink);line-height:1}
.site-search{position:absolute;left:792px;top:12px;display:flex;align-items:center;width:128px;height:20px;border:1px solid #cfcfcf;border-radius:10px;background:#fff;padding:0 6px 0 9px}
.site-search input{border:0;outline:0;background:transparent;width:96px;font:10px "Arimo",Arial,sans-serif;color:#777}
.site-search svg{margin-left:auto}
.main-nav{position:absolute;left:420px;top:46px;display:flex;align-items:center}
.main-nav a{font-family:"Hind",sans-serif;font-weight:600;font-size:12.5px;letter-spacing:.4px;color:#444;text-decoration:none;text-transform:uppercase;line-height:30px;margin-left:51px}
.main-nav .current{color:var(--orange);width:87px;height:30px;border-radius:15px;text-align:center;background:linear-gradient(#fff,#ececec);box-shadow:0 1px 3px rgba(0,0,0,.35);margin-left:0}
.main-nav .current+a{margin-left:36px}

.hero{position:absolute;left:0;top:126px;width:1043px;height:416px;background:var(--red)}
.hero-photo{position:absolute;left:103px;top:35px;width:835px;height:330px;
  background:
    linear-gradient(180deg,rgba(0,0,0,0) 45%,rgba(30,32,36,.35) 100%),
    linear-gradient(90deg,#c9cacb 0%,#4a4c50 14%,#6f7276 24%,#d8d9db 33%,#55595f 40%,#8d99a8 50%,#4e5258 60%,#d9dadc 66%,#2f3236 74%,#eef0f2 84%,#3a3d41 92%,#dcdcdc 100%)}
.hero-shadow{position:absolute;left:120px;top:367px;width:800px;height:18px;border-radius:50%;background:radial-gradient(ellipse,rgba(0,0,0,.28),rgba(0,0,0,0) 70%)}
.slide-btn{position:absolute;top:177px;width:52px;height:52px;background:rgba(120,120,120,.45)}
.slide-btn.prev{left:111px}
.slide-btn.next{left:875px}
.slide-btn svg{position:absolute;left:19px;top:16px}

.intro{position:absolute;left:104px;top:558px;width:548px}
.section-title{font-family:"Questrial",sans-serif;font-size:18px;color:var(--ink);font-weight:400;margin:0 0 0 2px;height:47px;line-height:26px}
.section-title em{font-style:normal;color:var(--red-text)}
.intro p{font-size:10.2px;line-height:15.6px;text-align:justify;margin-bottom:15.6px}
.divider{position:absolute;left:660px;top:558px;width:1px;height:240px;background:var(--rule)}
.services{position:absolute;left:669px;top:558px;width:270px}
.services p{font-size:10.2px;line-height:15.6px;text-align:justify;color:var(--muted)}
.check-list{list-style:none;margin-top:6px}
.check-list li{position:relative;padding-left:31px;font-size:10.2px;line-height:24.3px;color:var(--muted)}
.check-list svg{position:absolute;left:11px;top:7px}

.band-rule{position:absolute;left:0;top:821px;width:1043px;height:5px;background:linear-gradient(#e2e2e2,#fff)}

.card{position:absolute;top:843px;width:261px;height:246px;background:#fff;box-shadow:0 0 3px rgba(0,0,0,.2)}
.card::after{content:"";position:absolute;left:30px;right:30px;bottom:-14px;height:12px;border-radius:50%;background:radial-gradient(ellipse,rgba(0,0,0,.15),rgba(0,0,0,0) 70%)}
.card-title{position:relative;height:42px;padding-left:11px;font-family:"Hind",sans-serif;font-weight:700;font-size:17.5px;line-height:46px;color:#fff;letter-spacing:.3px}
.card-title::after{content:"";position:absolute;right:25px;bottom:-8px;border:8px solid transparent;border-bottom:0;border-top-color:inherit}
.card.strategy .card-title{background:linear-gradient(#d4c51a,var(--strategy));border-top-color:var(--strategy)}
.card.success .card-title{background:linear-gradient(#d6a81c,var(--success));border-top-color:var(--success)}
.card.goal .card-title{background:linear-gradient(#d4741a,var(--goal));border-top-color:var(--goal)}
.card-image{height:101px;margin:0 1px}
.card.strategy .card-image{background:radial-gradient(circle at 50% 40%,#cfe4ff,#3a6fc4 45%,#0e2352 90%)}
.card.success .card-image{background:linear-gradient(90deg,#2a2a2a,#7a7a6c 30%,#0d0d0d 65%,#050505)}
.card.goal .card-image{background:radial-gradient(circle at 30% 45%,#3c7a3a,#5e5e5e 40%,#9a9a9a 80%)}
.card-text{padding:7px 6px 0 10px;font-size:10.3px;line-height:15.6px;text-align:justify;color:var(--muted)}
.card-more{position:absolute;left:9px;top:222px;font-size:9.5px;font-weight:700;color:var(--ink);text-decoration:none;display:flex;align-items:center;gap:4px}
.card.strategy{left:104px}
.card.success{left:391px}
.card.goal{left:678px}

.site-footer{position:absolute;left:0;top:1138px;width:1043px;height:62px;background:var(--footer)}
.copyright{position:absolute;left:104px;top:24px;font-size:10.5px;color:#e6e6e6}
.social{position:absolute;left:834px;top:15px;display:flex;gap:4px}
.social span{width:29px;height:29px;border-radius:50%;background:#2a7fc4;border:2px solid #e8e8e8}
.social span:first-child{background:#3b5998}
.social span:nth-child(2){background:#1da1f2}
</style>
</head>
<body>
<div class="page">
  <header class="site-header">
    <div class="brand"><span class="brand-dot"></span><span class="brand-name">Vectorline Solutions</span></div>
    <form class="site-search" role="search">
      <input type="text" placeholder="Search site &amp; documents" aria-label="Search site content">
      <svg width="10" height="10" viewBox="0 0 10 10"><circle cx="4" cy="4" r="3" fill="none" stroke="#777" stroke-width="1.3"/><path d="M6.2 6.2L9 9" stroke="#777" stroke-width="1.4"/></svg>
    </form>
    <nav class="main-nav">
      <a class="current" href="#">About us</a>
      <a href="#">Services</a>
      <a href="#">Products</a>
      <a href="#">Careers</a>
      <a href="#">Contact</a>
    </nav>
  </header>

  <section class="hero">
    <div class="hero-shadow"></div>
    <div class="hero-photo" role="img" aria-label="Photo of three smiling team members in business attire"></div>
    <a class="slide-btn prev" href="#" aria-label="Previous slide"><svg width="14" height="20" viewBox="0 0 14 20"><path d="M11 2L3 10l8 8" fill="none" stroke="#ddd" stroke-width="2.5"/></svg></a>
    <a class="slide-btn next" href="#" aria-label="Next slide"><svg width="14" height="20" viewBox="0 0 14 20"><path d="M3 2l8 8-8 8" fill="none" stroke="#ddd" stroke-width="2.5"/></svg></a>
  </section>

  <section class="intro">
    <h1 class="section-title">Welcome to <em>Vectorline Solution</em></h1>
    <p>Lorem ipsum dolor sit amet, consectetuer adipiscing elit. Praesent vestibulum molestie lacus. Aenean nonummy hendrerit mauris. Phasellus porta. Fusce suscipit varius mi. Cum sociis natoque penatibus et magnis dis parturient montes, nascetur ridiculus mus.</p>
    <p>Quisque gravida bibendum magna fermenm eleifend. Donec erat justo, blant non hendrerit sed, consequat ut velit. Vestibulum sed nisi eget mauris interdum adipiscing...Lorem ipsum dolor sit amet, consectetuer adipiscing elit. Praesent vestibulum molestie lacus. Aenean nonummy hendrerit mauris. Phasellus porta. Fusce suscipit varius mi. Cum sociis natoque penatibus et magnis dis parturient montes, nascetur ridiculus mus. Lorem ipsum dolor sit amet, consectetuer adipiscing elit. Praesent vestibulum molestie lacus. Aenean nonummy hendrerit mauris. Phasellus porta. Fusce suscipit varius mi. Cum sociis natoque penatibus et magnis dis parturient montes, nascetur ridiculus mus. Lorem ipsum dolor sit amet, consectetuer adipiscing elit. Praesent vestibulum molestie lacus. Aenean nonummy hendrerit mauris. Phasellus porta. Fusce suscipit varius mi. Cum sociis natoque penatibus et magnis dis parturient montes, nascetur ridiculus mus.</p>
  </section>
  <div class="divider"></div>
  <aside class="services">
    <h2 class="section-title">Services</h2>
    <p>At vero eos et accusamus et iusto odio dignissimos ducimus qui blanditiis praesentium voluptatum deleniti atque corruptvoluptatum deleniti atque corrupti deleniti atque corrupti</p>
    <ul class="check-list">
      <li><svg width="11" height="10" viewBox="0 0 11 10"><rect x=".5" y="1.5" width="8" height="8" fill="none" stroke="#555"/><path d="M2 5l2.5 3L10 1" fill="none" stroke="#222" stroke-width="1.6"/></svg>qui blanditiis praesentium voluptatum</li>
      <li><svg width="11" height="10" viewBox="0 0 11 10"><rect x=".5" y="1.5" width="8" height="8" fill="none" stroke="#555"/><path d="M2 5l2.5 3L10 1" fill="none" stroke="#222" stroke-width="1.6"/></svg>deleniti atque corruptvoluptatum</li>
      <li><svg width="11" height="10" viewBox="0 0 11 10"><rect x=".5" y="1.5" width="8" height="8" fill="none" stroke="#555"/><path d="M2 5l2.5 3L10 1" fill="none" stroke="#222" stroke-width="1.6"/></svg>deleniti atque corruptatque corrupti</li>
      <li><svg width="11" height="10" viewBox="0 0 11 10"><rect x=".5" y="1.5" width="8" height="8" fill="none" stroke="#555"/><path d="M2 5l2.5 3L10 1" fill="none" stroke="#222" stroke-width="1.6"/></svg>qui blanditiis praesentium voluptatum</li>
      <li><svg width="11" height="10" viewBox="0 0 11 10"><rect x=".5" y="1.5" width="8" height="8" fill="none" stroke="#555"/><path d="M2 5l2.5 3L10 1" fill="none" stroke="#222" stroke-width="1.6"/></svg>deleniti atque corruptvoluptatum</li>
    </ul>
  </aside>

  <div class="band-rule"></div>

  <article class="card strategy">
    <h3 class="card-title">OUR STRATEGY</h3>
    <div class="card-image" role="img" aria-label="Photo of a hand placing a glowing blue puzzle piece"></div>
    <p class="card-text">varius mi. Cum sociis natoque penatibus et magnis dis parturient montes, nascetur ridiculus mus. Lorem ipsum dolor sit amet, consectetuer adipiscing elit.</p>
    <a class="card-more" href="#">MORE <svg width="9" height="8" viewBox="0 0 9 8"><path d="M0 4h8M5 1l3 3-3 3" fill="none" stroke="#222" stroke-width="1.2"/></svg></a>
  </article>
  <article class="card success">
    <h3 class="card-title">OUR SUCCESS</h3>
    <div class="card-image" role="img" aria-label="Photo of fingers walking up a stack of banknotes"></div>
    <p class="card-text">varius mi. Cum sociis natoque penatibus et magnis dis parturient montes, nascetur ridiculus mus. Lorem ipsum dolor sit amet, consectetuer adipiscing elit</p>
    <a class="card-more" href="#">MORE <svg width="9" height="8" viewBox="0 0 9 8"><path d="M0 4h8M5 1l3 3-3 3" fill="none" stroke="#222" stroke-width="1.2"/></svg></a>
  </article>
  <article class="card goal">
    <h3 class="card-title">OUR GOAL</h3>
    <div class="card-image" role="img" aria-label="Photo of a dart hitting the bullseye of a dartboard"></div>
    <p class="card-text">varius mi. Cum sociis natoque penatibus et magnis dis parturient montes, nascetur ridiculus mus. Lorem ipsum dolor sit amet, consectetuer adipiscing elit.</p>
    <a class="card-more" href="#">MORE <svg width="9" height="8" viewBox="0 0 9 8"><path d="M0 4h8M5 1l3 3-3 3" fill="none" stroke="#222" stroke-width="1.2"/></svg></a>
  </article>

  <footer class="site-footer">
    <p class="copyright">© Copyright 2012&nbsp; Vectorline Solutions</p>
    <div class="social" aria-label="Social links"><span></span><span></span><span></span></div>
  </footer>
</div>
</body>
</html>
```